Bannerdesign
Zielgruppe
Ich biete Fort- und Ausbildungen für Tiertherapeuten an. Schwerpunkte der Ausbildung sind Akupunktur oder Osteopathie für Pferde und Hunde. Meine Zielgruppe sind Frauen, die Tiere lieben bzw. schon selbst Tiertherapeutinnen sind. Zielgruppenalter 30-50 Jahre.
Aufgabenstellung
Ich wünsche ein Banner, um mich mit anderen Kollegen/Firmen zu vernetzen. Das Banner soll auf ihren Seiten erscheinen und im Gegenzug verlinke ich mich mit ihrem Banner.
Im Banner soll zu ersehen sein, dass ich Seminare anbiete. Der Name Fell-Akademie sollte auftauchen, sowie www.fell-akademie.de
Der Slogan heißt: Tierisch viel Wissen.

```html
<!DOCTYPE html>
<html lang="de">
<head>
<meta charset="utf-8">
<title>Fell-Akademie – Bannerset</title>
<link href="https://fonts.googleapis.com/css2?family=Roboto:wght@400;500;700;900&display=swap" rel="stylesheet">
<style>
  :root{
    --teal:#41c0d8;
    --logo-teal:#2cb3cb;
    --navy:#0f4466;
    --label:#1f5878;
    --gold-band:#e3d096;
    --gold-text:#bf9440;
    --white:#ffffff;
    --frame:#d3dadd;
    --snow-1:#eef3f7;
    --snow-2:#c9d6e0;
  }
  *{margin:0;padding:0;box-sizing:border-box}
  html,body{width:1002px;height:1200px;overflow:hidden;background:var(--white)}
  body{position:relative;font-family:"Roboto",Arial,sans-serif;color:var(--navy)}
  .size-label{position:absolute;font-size:19px;font-weight:500;color:var(--label);letter-spacing:.2px}
  .banner{position:absolute;background:var(--teal);overflow:hidden;box-shadow:0 0 0 1px var(--frame)}
  .shapes,.photo{position:absolute;inset:0;width:100%;height:100%}
  .brand{position:absolute;text-align:center;line-height:1}
  .brand-name{display:block;color:var(--logo-teal);font-weight:400;letter-spacing:.3px;white-space:nowrap}
  .brand-tagline{display:block;color:var(--gold-text);font-weight:400;white-space:nowrap}
  .headline{position:absolute;color:var(--navy);font-weight:700;line-height:1.12;white-space:nowrap}
  .subline{position:absolute;color:var(--white);font-weight:500;line-height:1.25;white-space:nowrap}
  .cta-band{position:absolute;background:var(--gold-band);color:var(--navy);display:flex;align-items:center;white-space:nowrap}
  .cta-band strong{font-weight:900}
  .species{position:absolute;color:var(--navy);line-height:1}
  .species .small{font-weight:400}
  .species .big{font-weight:700}
</style>
</head>
<body>

<!-- 468 x 60 -->
<div class="size-label" style="left:28px;top:16px">468 x 60px</div>
<div class="banner" style="left:28px;top:45px;width:655px;height:84px">
  <svg class="shapes" viewBox="0 0 655 84" aria-hidden="true">
    <path d="M0 0H130Q150 42 136 84H0Z" fill="var(--white)"/>
    <path d="M133 0Q155 42 140 84" fill="none" stroke="var(--navy)" stroke-width="5"/>
  </svg>
  <svg class="photo" viewBox="0 0 655 84" role="img" aria-label="Foto: Pferd und Hund toben im Schnee">
    <defs><linearGradient id="snowA" x1="0" y1="0" x2="0" y2="1"><stop offset="0" stop-color="var(--snow-2)"/><stop offset=".6" stop-color="var(--snow-1)"/><stop offset="1" stop-color="#fff"/></linearGradient></defs>
    <path d="M516 0H655V84H524Q504 42 516 0Z" fill="url(#snowA)"/>
    <path d="M512 0Q500 42 520 84" fill="none" stroke="var(--navy)" stroke-width="4"/>
  </svg>
  <div class="brand" style="left:6px;top:28px;width:122px">
    <span class="brand-name" style="font-size:19px">Fell-Akademie</span>
    <span class="brand-tagline" style="font-size:8.5px;margin-top:4px">Tierisch viel Wissen</span>
  </div>
  <div class="headline" style="left:152px;top:10px;font-size:21px">Tierisch viel Wissen</div>
  <div class="subline" style="left:152px;top:37px;font-size:11px">Fort- und Ausbildung und Seminare für Tiertherapeuten</div>
  <div class="species" style="left:434px;top:7px;font-size:10px">
    <span class="small">Für</span><span class="big" style="font-size:13px">Hund</span><br>
    <span class="small" style="margin-left:12px">und</span><span class="big" style="font-size:13px">Pferd</span>
  </div>
  <div class="cta-band" style="left:145px;top:58px;width:375px;height:18px;justify-content:flex-end;padding-right:10px;font-size:9.5px;font-weight:500">
    Jetzt informieren unter:&nbsp;<strong style="font-size:12.5px">www.fell-akademie.de</strong>
  </div>
</div>

<!-- 234 x 60 -->
<div class="size-label" style="left:22px;top:219px">234 x 60px</div>
<div class="banner" style="left:22px;top:249px;width:436px;height:113px">
  <svg class="shapes" viewBox="0 0 436 113" aria-hidden="true">
    <path d="M0 0H168Q192 56 172 113H0Z" fill="var(--white)"/>
    <path d="M172 0Q198 56 178 113" fill="none" stroke="var(--navy)" stroke-width="6"/>
  </svg>
  <div class="brand" style="left:6px;top:38px;width:160px">
    <span class="brand-name" style="font-size:25px">Fell-Akademie</span>
    <span class="brand-tagline" style="font-size:11px;margin-top:6px">Tierisch viel Wissen</span>
  </div>
  <div class="headline" style="left:193px;top:10px;font-size:22px">Tierisch viel Wissen</div>
  <div class="subline" style="left:193px;top:38px;font-size:13px;line-height:1.2">Fort- und Ausbildung und Seminare<br>für Tiertherapeuten</div>
  <div class="cta-band" style="left:180px;top:75px;width:256px;height:23px;padding-left:12px;font-size:10px;font-weight:500">
    Jetzt informieren unter:&nbsp;<strong style="font-size:13px">www.fell-akademie.de</strong>
  </div>
</div>

<!-- 120 x 60 -->
<div class="size-label" style="left:475px;top:219px">120 x 60px</div>
<div class="banner" style="left:480px;top:249px;width:224px;height:113px">
  <svg class="shapes" viewBox="0 0 224 113" aria-hidden="true">
    <path d="M0 0H100Q118 46 104 95H0Z" fill="var(--white)"/>
    <path d="M104 0Q122 46 108 95" fill="none" stroke="var(--navy)" stroke-width="4"/>
  </svg>
  <div class="brand" style="left:3px;top:40px;width:98px">
    <span class="brand-name" style="font-size:13px">Fell-Akademie</span>
    <span class="brand-tagline" style="font-size:7px;margin-top:4px">Tierisch viel Wissen</span>
  </div>
  <div class="headline" style="left:116px;top:7px;font-size:16px;line-height:1.2">Tierisch<br>viel Wissen</div>
  <div class="subline" style="left:116px;top:49px;font-size:10.5px;line-height:1.25">Fort- und Ausbildung<br>und Seminare für<br>Tiertherapeuten</div>
  <div class="cta-band" style="left:0;top:94px;width:224px;height:16px;padding-left:5px;font-size:8.5px;font-weight:500">
    Jetzt informieren unter:&nbsp;<strong style="font-size:11px">www.fell-akademie.de</strong>
  </div>
</div>

<!-- 81 x 31 -->
<div class="size-label" style="left:538px;top:469px">81 x 31px</div>
<div class="banner" style="left:538px;top:499px;width:165px;height:59px">
  <svg class="shapes" viewBox="0 0 165 59" aria-hidden="true">
    <path d="M0 0H68Q80 26 70 52H0Z" fill="var(--white)"/>
    <path d="M70 0Q83 26 73 52" fill="none" stroke="var(--navy)" stroke-width="2.5"/>
  </svg>
  <div class="brand" style="left:2px;top:20px;width:66px">
    <span class="brand-name" style="font-size:9px">Fell-Akademie</span>
    <span class="brand-tagline" style="font-size:5px;margin-top:2px">Tierisch viel Wissen</span>
  </div>
  <div class="headline" style="left:77px;top:4px;font-size:9px">Tierisch viel Wissen</div>
  <div class="subline" style="left:77px;top:16px;font-size:5.5px;line-height:7px">Fort- und Ausbildung und<br>Seminare für Tiertherapeuten</div>
  <div class="cta-band" style="left:74px;top:34px;width:91px;height:18px;padding-left:3px;flex-direction:column;align-items:flex-start;justify-content:center">
    <span style="display:block;font-size:5px;font-weight:500;line-height:7px">Jetzt informieren unter:</span>
    <strong style="display:block;font-size:6.5px;line-height:8px">www.fell-akademie.de</strong>
  </div>
</div>

<!-- 125 x 125 -->
<div class="size-label" style="left:22px;top:469px">125 x 125px</div>
<div class="banner" style="left:22px;top:499px;width:234px;height:233px">
  <svg class="photo" viewBox="0 0 234 233" role="img" aria-label="Foto: Pferd und Hund toben im Schnee">
    <defs><linearGradient id="snowD" x1="0" y1="0" x2="0" y2="1"><stop offset="0" stop-color="var(--snow-2)"/><stop offset=".55" stop-color="var(--snow-1)"/><stop offset="1" stop-color="#fff"/></linearGradient></defs>
    <path d="M140 0H234V98Q195 104 166 95Q185 45 140 0Z" fill="url(#snowD)"/>
  </svg>
  <svg class="shapes" viewBox="0 0 234 233" aria-hidden="true">
    <path d="M0 0H142Q190 50 160 95Q120 130 0 112Z" fill="var(--white)"/>
    <path d="M0 110Q120 132 160 97Q178 78 168 52" fill="none" stroke="var(--navy)" stroke-width="4"/>
  </svg>
  <div class="brand" style="left:6px;top:58px;width:150px">
    <span class="brand-name" style="font-size:22px">Fell-Akademie</span>
    <span class="brand-tagline" style="font-size:10.5px;margin-top:6px">Tierisch viel Wissen</span>
  </div>
  <div class="species" style="left:152px;top:110px;font-size:12px">
    <span class="small">Für</span><span class="big" style="font-size:15px">Hund</span><br>
    <span class="small" style="margin-left:13px">und</span><span class="big" style="font-size:15px">Pferd</span>
  </div>
  <div class="headline" style="left:11px;top:151px;font-size:19px">Tierisch viel Wissen</div>
  <div class="subline" style="left:11px;top:176px;font-size:11.5px;line-height:14px">Fort- und Ausbildung und Seminare<br>für Tiertherapeuten</div>
  <div class="cta-band" style="left:0;top:209px;width:234px;height:17px;padding-left:10px;font-size:9px;font-weight:500">
    Jetzt informieren unter:&nbsp;<strong style="font-size:12px">www.fell-akademie.de</strong>
  </div>
</div>

<!-- 120 x 240 -->
<div class="size-label" style="left:292px;top:469px">120 x 240px</div>
<div class="banner" style="left:293px;top:499px;width:224px;height:447px">
  <svg class="shapes" viewBox="0 0 224 447" aria-hidden="true">
    <path d="M0 0H224V158Q130 215 0 170Z" fill="var(--white)"/>
    <path d="M40 196Q150 212 224 160" fill="none" stroke="var(--navy)" stroke-width="6"/>
  </svg>
  <div class="brand" style="left:0;top:92px;width:224px">
    <span class="brand-name" style="font-size:28px">Fell-Akademie</span>
    <span class="brand-tagline" style="font-size:14px;margin-top:8px">Tierisch viel Wissen</span>
  </div>
  <div class="headline" style="left:15px;top:226px;font-size:30px;line-height:1.12">Tierisch<br>viel Wissen</div>
  <div class="subline" style="left:15px;top:300px;font-size:19.5px;line-height:24px">Fort- und Ausbildung<br>und Seminare für<br>Tiertherapeuten</div>
  <div class="cta-band" style="left:0;top:381px;width:224px;height:52px;padding-left:15px;flex-direction:column;align-items:flex-start;justify-content:center;line-height:1.25">
    <span style="font-size:16px;font-weight:400">Jetzt informieren unter:</span>
    <strong style="font-size:19.5px">www.fell-akademie.de</strong>
  </div>
</div>

<!-- 120 x 90 -->
<div class="size-label" style="left:22px;top:966px">120 x 90px</div>
<div class="banner" style="left:22px;top:997px;width:224px;height:167px">
  <svg class="photo" viewBox="0 0 224 167" role="img" aria-label="Foto: Pferd und Hund toben im Schnee">
    <defs><linearGradient id="snowG" x1="0" y1="0" x2="0" y2="1"><stop offset="0" stop-color="var(--snow-2)"/><stop offset=".6" stop-color="var(--snow-1)"/><stop offset="1" stop-color="#fff"/></linearGradient></defs>
    <path d="M112 0H224V77Q170 82 118 74Q140 35 112 0Z" fill="url(#snowG)"/>
  </svg>
  <svg class="shapes" viewBox="0 0 224 167" aria-hidden="true">
    <path d="M0 0H114Q150 38 118 72Q80 90 0 82Z" fill="var(--white)"/>
    <path d="M0 83Q150 96 224 77" fill="none" stroke="var(--navy)" stroke-width="3.5"/>
  </svg>
  <div class="brand" style="left:4px;top:44px;width:114px">
    <span class="brand-name" style="font-size:16px">Fell-Akademie</span>
    <span class="brand-tagline" style="font-size:8px;margin-top:4px">Tierisch viel Wissen</span>
  </div>
  <div class="headline" style="left:10px;top:98px;font-size:16px">Tierisch viel Wissen</div>
  <div class="subline" style="left:10px;top:119px;font-size:10.5px;line-height:13px">Fort- und Ausbildung und Seminare<br>für Tiertherapeuten</div>
  <div class="cta-band" style="left:0;top:147px;width:224px;height:15px;padding-left:10px;font-size:8px;font-weight:500">
    Jetzt informieren unter:&nbsp;<strong style="font-size:11px">www.fell-akademie.de</strong>
  </div>
</div>

<!-- 120 x 600 -->
<div class="size-label" style="left:741px;top:16px">120 x 600px</div>
<div class="banner" style="left:742px;top:45px;width:224px;height:1117px">
  <svg class="photo" viewBox="0 0 224 1117" role="img" aria-label="Foto: Pferd und Hund toben im Schnee">
    <defs><linearGradient id="snowH" x1="0" y1="0" x2="0" y2="1"><stop offset="0" stop-color="#dfe7ee"/><stop offset=".35" stop-color="var(--snow-2)"/><stop offset=".7" stop-color="#d8cfc7"/><stop offset="1" stop-color="#f4f6f8"/></linearGradient></defs>
    <path d="M0 800Q130 845 224 805V1117H0Z" fill="url(#snowH)"/>
  </svg>
  <svg class="shapes" viewBox="0 0 224 1117" aria-hidden="true">
    <path d="M0 0H224V170Q110 240 0 200Z" fill="var(--white)"/>
    <path d="M30 222Q150 240 224 185" fill="none" stroke="var(--navy)" stroke-width="6"/>
    <path d="M0 790Q120 835 224 790V808Q130 850 0 812Z" fill="var(--white)"/>
    <path d="M0 790Q110 840 224 805" fill="none" stroke="var(--navy)" stroke-width="5"/>
  </svg>
  <div class="brand" style="left:0;top:110px;width:224px">
    <span class="brand-name" style="font-size:28px">Fell-Akademie</span>
    <span class="brand-tagline" style="font-size:15px;margin-top:9px">Tierisch viel Wissen</span>
  </div>
  <div class="headline" style="left:14px;top:252px;font-size:38px;line-height:1.3">Tierisch<br>viel Wissen</div>
  <div class="subline" style="left:14px;top:366px;font-size:25px;line-height:1.6">Fort- und Aus-<br>bildung und<br>Seminare für<br>Tiertherapeuten</div>
  <div class="species" style="left:48px;top:597px;font-size:21px">
    <span class="small">Für</span><span class="big" style="font-size:26px">Hund</span><br>
    <span class="small" style="margin-left:22px">und</span><span class="big" style="font-size:26px">Pferd</span>
  </div>
  <div class="cta-band" style="left:0;top:706px;width:224px;height:58px;padding-left:9px;flex-direction:column;align-items:flex-start;justify-content:center;line-height:1.25">
    <span style="font-size:17px;font-weight:400">Jetzt informieren unter:</span>
    <strong style="font-size:19px">www.fell-akademie.de</strong>
  </div>
</div>

</body>
</html>
```